Brochure for a civil enineering company in A4 format

I need a brochure design for our company VELTA Engineering S.r.l.. We are an engineering consultant company. Our main clients are from the infrastructure industry (geotechnical and underground sectors mainly).
We are looking for a 2 pages (4 faces) fold out design with a glued pocket where we can put individual data sheets.
I need A4 format pages.

Target Market(s)

We are an engineering consultant company. Our main clients are from the infrastructure industry (geotechnical and underground sectors mainly).

Industry/Entity Type

Civil Engineer

Font styles to use
Sans Serif

Requirements
Must have
• Overall: 2 pages in A4 format
Essential style. Bright and modern appearance.
Glued pocket
Logo integrated in a picture on the pocket where I would like to insert a slogan (… velta engineering … reliable solutions …)
Attached are selected images which the designer can use and edit at their own discretion.
Some advice in the following (anyway designers are free to provide their solutions):
Outer sheets:
Front page with name, logo. It could be nice to have the “m” of the logo integrated in a pictures, also a modified picture (I mean modify one of the attached pictures) so to create a general image and do not tie the cover to a specific job.
Back page: offices address and contact email address. Nice to have one space for a slogan.
Inner sheet: text that I upload in the file “inside-sheets”, possibly with pictures on each sheet. In the right faces insert the glued pocket. On this pages insert the section OUR EXPERIENCE ….with a space for a picture of our team.
Nice to have
• Clean and essential design.
Pictures choosing from the atteched ones. Pictures could be modified in a very light manner to make them a general idea of the work ( I mean geotechnical world) without to be immediately linked to a specific site.
Should not have
• excessive frills

```html
<!DOCTYPE html>
<html lang="it">
<head>
<meta charset="utf-8">
<title>VELTA Engineering – Brochure</title>
<link href="https://fonts.googleapis.com/css2?family=Montserrat:wght@300;400;500;600&family=Oswald:wght@400&display=swap" rel="stylesheet">
<style>
:root{
  --bg:#d6d6d6;
  --page:#f4f4f4;
  --page-light:#fbfbfb;
  --ink:#1d1d1d;
  --text:#555;
  --muted:#8a8a8a;
  --rule:#3a3a3a;
  --tile:#e6e6e6;
}
*{margin:0;padding:0;box-sizing:border-box}
html,body{width:888px;height:1200px;overflow:hidden;background:var(--bg)}
body{position:relative;font-family:"Montserrat",sans-serif;color:var(--text)}
.spread{position:absolute;left:101px;width:685px;height:484px;background:linear-gradient(90deg,#eeeeee 0%,#f5f5f5 50%,var(--page-light) 50%,#f7f7f7 100%);overflow:hidden;box-shadow:0 6px 14px rgba(0,0,0,.18)}
.spread--outer{top:78px}
.spread--inner{top:638px}
.fold{position:absolute;left:342px;top:0;width:1px;height:100%;background:rgba(0,0,0,.04)}
.abs{position:absolute}
.photo{position:absolute}
.hatch-panel{left:104px;top:38px;width:171px;height:172px;background:#e4e4e4}
.wordmark{font-family:"Montserrat",sans-serif;font-weight:600;color:#2b2b2b;letter-spacing:.02em}
.wordmark--cover{left:447px;top:30px;font-size:34px}
.wordmark--back{left:232px;top:432px;font-size:17px}
.photo-frame{left:225px;top:101px;width:460px;height:282px;background:#fff}
.slogan{left:378px;top:423px;font-family:"Oswald",sans-serif;font-size:13.5px;color:var(--ink);letter-spacing:.01em;white-space:nowrap}
.section-title{font-size:12.5px;font-weight:300;color:var(--ink);letter-spacing:.02em;white-space:nowrap}
.section-title b{font-weight:600}
.rule{height:.8px;background:var(--rule)}
.offices{left:35px;top:299px;width:151px}
.offices .rule{margin-top:4px}
.office{margin-top:6px;margin-left:11px;font-size:6.6px;line-height:8.8px;color:var(--ink);font-weight:500}
.contact{position:relative}
.contact svg{position:absolute;left:-10px;top:1px;width:6px;height:6px}
.office + .office{margin-top:9px}
.web{margin-top:10px}
.body-col{width:272px}
.body-col p{font-size:5.7px;line-height:8px;text-align:justify;font-weight:300;color:var(--text);margin-bottom:8px}
.body-col p.lead{font-weight:500;color:var(--ink)}
.body-col .rule{margin:4px 0 6px}
.company{left:35px;top:26px}
.services{left:35px;top:208px}
.service-list{left:122px;top:368px;width:185px}
.service-list p{font-size:5.2px;line-height:7.2px;text-align:justify;font-weight:300;color:var(--text);margin-bottom:8px}
.expertise{left:377px;top:26px}
.founders-tag{left:376px;top:102px;width:149px;height:13px;background:var(--ink);color:#fff;font-size:8px;font-weight:500;padding:2px 0 0 11px;clip-path:polygon(0 0,92% 0,100% 100%,0 100%)}
.founders-rule{left:520px;top:114px;width:129px;height:.8px;background:var(--rule)}
.founders{left:377px;top:122px;width:272px}
.founders p{font-size:5px;line-height:7.1px;text-align:justify;font-weight:300;color:var(--text);margin-bottom:7px}
.base-bar{left:0;top:480px;width:342px;height:4px;background:var(--ink)}
</style>
</head>
<body>

<section class="spread spread--outer">
  <div class="fold"></div>
  <div class="abs hatch-panel" role="img" aria-label="Pannello decorativo tratteggiato"></div>

  <div class="abs offices">
    <h2 class="section-title">OUR <b>OFFICES</b></h2>
    <div class="rule"></div>
    <div class="office">
      <div>Milano</div>
      <div class="contact"><svg viewBox="0 0 10 10"><circle cx="5" cy="3.5" r="2.5" fill="none" stroke="#222" stroke-width="1"/><path d="M5 6v3M3 9h4" stroke="#222" stroke-width="1"/></svg>Via Lanterna, 14<br>20121 Milano - IT</div>
      <div class="contact" style="margin-top:3px"><svg viewBox="0 0 10 10"><circle cx="5" cy="5" r="4.3" fill="none" stroke="#222" stroke-width=".9"/><path d="M3.5 3c0 2 1.5 3.5 3.5 3.5" stroke="#222" stroke-width="1" fill="none"/></svg>+39 02 555010101</div>
      <div class="contact"><svg viewBox="0 0 10 10"><rect x=".5" y="2" width="9" height="6" fill="none" stroke="#222" stroke-width=".9"/><path d="M.5 2l4.5 3.5L9.5 2" stroke="#222" stroke-width=".9" fill="none"/></svg>info@veltaengineering.example</div>
    </div>
    <div class="office">
      <div>Arco TN</div>
      <div class="contact"><svg viewBox="0 0 10 10"><circle cx="5" cy="3.5" r="2.5" fill="none" stroke="#222" stroke-width="1"/><path d="M5 6v3M3 9h4" stroke="#222" stroke-width="1"/></svg>Via dei Colli, 9<br>38062 Arco TN - IT</div>
      <div class="contact" style="margin-top:3px"><svg viewBox="0 0 10 10"><circle cx="5" cy="5" r="4.3" fill="none" stroke="#222" stroke-width=".9"/><path d="M3.5 3c0 2 1.5 3.5 3.5 3.5" stroke="#222" stroke-width="1" fill="none"/></svg>+39 02 555010101</div>
      <div class="contact"><svg viewBox="0 0 10 10"><rect x=".5" y="2" width="9" height="6" fill="none" stroke="#222" stroke-width=".9"/><path d="M.5 2l4.5 3.5L9.5 2" stroke="#222" stroke-width=".9" fill="none"/></svg>info@veltaengineering.example</div>
    </div>
    <div class="office web">
      <div class="contact"><svg viewBox="0 0 10 10"><circle cx="5" cy="5" r="4.2" fill="none" stroke="#222" stroke-width=".9"/><path d="M.8 5h8.4M5 .8c-2.4 2.6-2.4 5.8 0 8.4M5 .8c2.4 2.6 2.4 5.8 0 8.4" stroke="#222" stroke-width=".7" fill="none"/></svg>www.veltaengineering.example</div>
    </div>
  </div>

  <div class="abs wordmark wordmark--back">VELTA</div>

  <div class="abs wordmark wordmark--cover">VELTA</div>
  <div class="abs photo-frame"></div>
  <div class="photo" style="left:232px;top:106px;width:277px;height:272px;background:linear-gradient(160deg,#8a7362 0%,#6b5a4e 35%,#3e3a3a 60%,#7d7f88 100%)" role="img" aria-label="Galleria in scavo con centine e rivestimento in calcestruzzo proiettato"></div>
  <div class="photo" style="left:513px;top:106px;width:167px;height:149px;background:linear-gradient(135deg,#a8a7a2 0%,#8d8a84 45%,#a46a4a 60%,#9b9893 100%)" role="img" aria-label="Vista aerea di un cantiere con gru e materiali da costruzione"></div>
  <div class="photo" style="left:513px;top:260px;width:167px;height:117px;background:linear-gradient(135deg,#6f7d5c 0%,#aeb0ab 35%,#c9c6c0 55%,#5f7a4c 100%)" role="img" aria-label="Vista aerea di un'area di cantiere circondata da vegetazione"></div>

  <div class="abs slogan">VELTA ENGINEERING, RELIABLE SOLUTIONS</div>
</section>

<section class="spread spread--inner">
  <div class="fold"></div>

  <div class="abs body-col company">
    <h2 class="section-title">OUR <b>COMPANY</b></h2>
    <div class="rule"></div>
    <p>VELTA Engineering S.r.l. offre servizi di consulenza tecnica, contrattuale e strategica ai principali attori nei settori delle scienze geologiche, dell'ingegneria geotecnica e dell'ingegneria idraulica. Lavoriamo per mitigare il rischio e ridurre l'incertezza, con flessibilità nella ricerca della soluzione ottimale contribuendo ad aumentare la redditività del progetto.</p>
    <p>VELTA Engineering S.r.l. è una società indipendente che nasce nel luglio 2020 dall'associazione di un gruppo di professionisti che hanno messo a fattor comune la reciproca esperienza maturata in oltre trent'anni di attività come progettisti e consulenti nel settore delle grandi opere di ingegneria civile lavorando come Direttori Tecnici di Main Engineering Companies and as Freelancers.</p>
    <p>VELTA Engineering S.r.l. vuole unire l'esperienza dei Fondatori e delle figure chiave con l'entusiasmo di chi intraprende una nuova attività, per dare vita ad una nuova realtà che si pone come obbiettivo principale il design of infrastructures that are safe, sustainable and economic.</p>
    <p>Each of our projects represents a long term commitment, we believe in providing safe, reliable, sustainable end innovative solutions. This is and will be our distinctive characteristic.</p>
  </div>

  <div class="abs body-col services">
    <h2 class="section-title">OUR <b>SERVICES</b></h2>
    <div class="rule"></div>
    <p>Progettazione e consulenza specialistica nel campo della geologia, dell'ingegneria geotecnica, delle opere sotterranee e dell'ingegneria idtraulica.</p>
    <p>Aiutiamo i nostri clienti a risolvere problemi di natura progettuale, contrattuale e costruttiva che possono nascere nell'intera vita del progetto portando la nostra esperienza all'interno delle loro organizzazioni, migliorando la qualità dei loro servizi di ingegneria, ottimizzando i loro progetti, proponendo nuove idee e soluzioni, rafforzando i loro approcci ......</p>
    <p>VELTA Engineering è in grado di fornire la propria assistenza nell'intero iter procedurale, dalla fase di indagine preliminare e di analisi di fattibilità fino alla progettazione costruttiva e all'assistenza tecnica in fase realizzativa.</p>
    <p class="lead">La specializzazione e l'esperienza accumulate nelle discipline della geologia, dell'ingegneria geotecnica e del sottosuolo e dell'idraulica ci permette di massimizzare la nostra efficacia quando sia necessario:</p>
  </div>

  <div class="photo" style="left:36px;top:366px;width:75px;height:46px;background:linear-gradient(160deg,#9aa0a2 0%,#6d6f6c 50%,#4a4d4e 100%)" role="img" aria-label="Scavo di un pozzo con imbocco di galleria"></div>
  <div class="photo" style="left:36px;top:417px;width:75px;height:46px;background:linear-gradient(180deg,#cfd5d8 0%,#a39486 40%,#6b625b 100%)" role="img" aria-label="Cantiere urbano davanti a un edificio storico"></div>

  <div class="abs service-list">
    <p>far fronte a situazioni di emergenza anche su progetti in fase di sviluppo avanzato garantendo l'immediata focalizzazione delle problematiche di progetto e garantendo il risultato finale atteso (in termini di qualità, tempistiche e costi...)</p>
    <p>fornire "second opinion" di elevato valore tecnico ed amministrativo in occasione di problematiche progettuali e costruttive e dispute legali</p>
    <p>analizzare in tempi brevi progetti svolti da terzi individuandone le "criticità", verificandone la cantierabilità e la validità tecnico economica.</p>
    <p>ottimizzare i progetti redatti da terzi implementandone il contenuto e massimizzando l'efficacia economica degli investimenti.</p>
  </div>
  <div class="abs base-bar"></div>

  <div class="abs body-col expertise">
    <h2 class="section-title">OUR <b>EXPERTISE AND EXPERIENCE</b></h2>
    <div class="rule"></div>
    <p>La società nasce dall'associazione di un gruppo di professionisti, con indiscusse competenze ed affidabilità, con esperienza maturata in oltre trent'anni di attività come progettisti e consulenti nel settore delle grandi opere di ingegneria civile; geologia, ingegneria geotecnica ed idraulica ed opere sotterranee sono il "core" delle loro competenze ....</p>
  </div>
  <div class="abs founders-tag">I SOCI FONDATORI SONO:</div>
  <div class="abs founders-rule"></div>
  <div class="abs founders">
    <p>Marco. Già Direttore Tecnico e Socio di Ardesia Srl, nel periodo di sua permanenza fino al dicembre 2018, ha per essa firmato tutti i progetti nel campo delle opere sotterranee e la maggior parte di quelli di ingegneria geotecnica. Da gennaio 2019 è Direttore Tecnico di GEOPRO. Può vantare più di 150 gallerie naturali, e numerosi progetti ed assistenze tecniche nel campo delle strutture geotecniche, delle sistemazioni idrogeologiche e dei versanti e delle opere di protezione ambientale. Negli ultimi dieci anni è stato responsabile di attività di assistenza tecnica, per imprese di costruzione, di opere il cui valore supera i 440 Mio EUR e di servizi di progettazione definitiva e/o esecutiva per opere il cui valore supera i 1.400 Mio EUR. Ha svolto attività di verifica e validazione, in Italia ed all'estero, di numerosi progetti il cui valore complessivo supera I 3.400 Mio EUR.</p>
    <p>Paolo 30 anni di esperienza professionale. Coinvolto in più di 150 gallerie naturali con lunghezza complessiva superiore a 360 km. Numerosi progetti ed attività di assistenza tecnica nel campo delle strutture, delle sistemazioni idrogeologiche e dei versanti e delle opere di protezione ambientale. Negli ultimi dieci anni responsabile di attività di assistenza tecnica in corso d'opera, per imprese di costruzione, di opere il cui valore supera i 440 Mio EUR e di servizi di progettazione definitiva o esecutiva per opere il cui valore supera I 1.400 Mio EUR. Ha svolto attività di verifica ai fini della validazione, in Italia ed all'estero, di numerosi progetti il cui valore complessivo supera I 3.400 Mio EUR.</p>
    <p>Giulia 30 anni di esperienza professionale. Coinvolto in più di 150 gallerie naturali con lunghezza complessiva superiore a 360 km. Numerosi progetti ed attività di assistenza tecnica nel campo delle strutture, delle sistemazioni idrogeologiche e dei versanti e delle opere di protezione ambientale. Negli ultimi dieci anni responsabile di attività di assistenza tecnica in corso d'opera, per imprese di costruzione, di opere il cui valore supera i 440 Mio EUR e di servizi di progettazione definitiva o esecutiva per opere il cui valore supera I 1.400 Mio EUR. Ha svolto attività di verifica ai ini della validazione, in Italia ed all'estero, di numerosi progetti il cui valore complessivo supera I 3.400 Mio EUR.</p>
    <p>Sara 30 anni di esperienza professionale. Coinvolto in più di 150 gallerie naturali con lunghezza complessiva superiore a 360 km. Numerosi progetti ed attività di assistenza tecnica nel campo delle strutture, delle sistemazioni idrogeologiche e dei versanti e delle opere di protezione ambientale. Negli ultimi dieci anni responsabile di attività di assistenza tecnica in corso d'opera, per imprese di costruzione, di opere il cui valore supera i 440 Mio EUR e di servizi di progettazione definitiva o esecutiva per opere il cui valore supera I 1.400 Mio EUR. Ha svolto attività di verifica ai fini della validazione, in Italia ed all'estero, di numerosi progetti il cui valore complessivo supera I 3.400 Mio EUR.</p>
  </div>

  <div class="photo" style="left:353px;top:381px;width:332px;height:103px;background:linear-gradient(180deg,#b9c9d8 0%,#c8c3b4 35%,#9c9584 65%,#6f6a60 100%);clip-path:polygon(20% 0,100% 0,100% 100%,0 100%)" role="img" aria-label="Imbocchi di due gallerie in un paesaggio collinare con gru di cantiere"></div>
</section>

</body>
</html>
```